Business Card Design Project

We are a very talented award winning hair salon, the card should be professional, classy with edge. Attached is the logo which I would like to see on one side, with text and something catchy on back.

Target Market(s)

Young professional, 20-50

Industry/Entity Type

Hair

Colors

Designer to choose colors to be used in the design.

Requirements
Must have
• Must be clean, exude professionalism, classy with some edge

```html
<!DOCTYPE html>
<html lang="en">
<head>
<meta charset="utf-8">
<title>Veyra Salon – Business Cards</title>
<link href="https://fonts.googleapis.com/css2?family=Cormorant+Garamond:wght@500&family=Open+Sans:wght@600&display=swap" rel="stylesheet">
<style>
  :root {
    --backdrop: #3a2c24;
    --card-light: #ffffff;
    --card-dark: #050505;
    --gold: #c9a227;
    --gold-light: #f3d65e;
    --gold-deep: #b08a1c;
    --ink: #1a1a1a;
    --name-brown: #8a6a1e;
  }
  * { margin: 0; padding: 0; box-sizing: border-box; }
  html, body { width: 1200px; height: 480px; overflow: hidden; }
  body { background: var(--backdrop); position: relative; }

  .card {
    position: absolute;
    width: 480px;
    height: 270px;
    overflow: hidden;
    box-shadow: 0 4px 14px rgba(0,0,0,.45);
  }
  .card--front { left: 86px; top: 100px; background: var(--card-light); }
  .card--back  { left: 586px; top: 99px; background: var(--card-dark); }

  .wordmark {
    position: absolute;
    left: 0; right: 0;
    height: 52px;
    display: flex;
    align-items: center;
    justify-content: center;
    gap: 14px;
  }
  .card--front .wordmark { top: 78px; }
  .card--back .wordmark  { top: 86px; }

  .wordmark__name {
    font-family: "Cormorant Garamond", serif;
    font-weight: 500;
    font-size: 40px;
    letter-spacing: 3px;
    line-height: 1;
    color: var(--gold);
    white-space: nowrap;
  }
  .wordmark__square {
    width: 46px;
    height: 46px;
    flex: none;
    background: var(--gold);
  }

  .holder {
    position: absolute;
    left: 0; right: 0;
    top: 208px;
    text-align: center;
    font-family: "Cormorant Garamond", serif;
    font-weight: 500;
    font-size: 17px;
    line-height: 1;
    color: var(--name-brown);
  }
  .holder__title { font-size: 13px; }

  .contact-band {
    position: absolute;
    left: 0; right: 0; bottom: 0;
    height: 30px;
    background: linear-gradient(90deg, var(--gold-deep), var(--gold-light) 45%, var(--gold) 100%);
    display: flex;
    align-items: center;
    justify-content: center;
    gap: 22px;
    font-family: "Open Sans", sans-serif;
    font-weight: 600;
    font-size: 10.5px;
    color: var(--ink);
    white-space: nowrap;
  }

  .gold-rule {
    position: absolute;
    left: 0; right: 0;
    bottom: 14px;
    height: 6px;
    background: linear-gradient(90deg, var(--gold-deep), var(--gold-light) 50%, var(--gold));
  }
</style>
</head>
<body>
  <section class="card card--front" aria-label="Business card front">
    <div class="wordmark">
      <span class="wordmark__name">VEYRA SALON</span>
      <span class="wordmark__square" aria-hidden="true"></span>
    </div>
    <p class="holder">Yourname Here, <span class="holder__title">Director</span></p>
    <div class="contact-band">
      <span>T: 012.555.0148</span>
      <span>E: info@veyrasalon.com</span>
      <span>www.veyrasalon.com</span>
    </div>
  </section>

  <section class="card card--back" aria-label="Business card back">
    <div class="wordmark">
      <span class="wordmark__name">VEYRA SALON</span>
      <span class="wordmark__square" aria-hidden="true"></span>
    </div>
    <div class="gold-rule" aria-hidden="true"></div>
  </section>
</body>
</html>
```